Full service meeting planning company needs new business cards

Velmora Linkway is a full service meeting planning company that specializes in on-line conference registration web development and event communications. We combine citywide hotel management, mobile applications, eblast reminders, confirmation letters, and customized reporting to create a seamless registration process. We also manage group motor coach transportation, food and beverages, entertainment, stage and lighting for group of 10 to 4000.

Target Market(s)

Corporations and associations

Industry/Entity Type

Event Planning

Contact Information for Business Card

standard size 3.5" wide and 2" tall

Font styles to use
Serif
Sans Serif

Colors
f37122
f78f20
333333
5c5c5c
9d9d9d
f68d4d

Requirements
Must have
• {name}
• Velmora Linkway
• P.O. Box 7384, Grand Rapids, M I 49568
• www.velmoralinkway.com
• {email}
• {phone}
• {mobile phone}
Nice to have
• Our colors are black, grey and orange as an accent color
Should not have
• I am not happy with our website layout anymore either. It feels dark and old but it does explain who we are pretty well if you'd like to review; www.velmoralinkway.com

```html
<!DOCTYPE html>
<html lang="en">
<head>
<meta charset="utf-8">
<title>Velmora Linkway – Business Cards</title>
<link href="https://fonts.googleapis.com/css2?family=Montserrat:wght@600;700&family=Open+Sans:wght@400;600;700&display=swap" rel="stylesheet">
<style>
  :root {
    --backdrop: #bdbdbd;
    --card-white: #ffffff;
    --card-black: #2b2b2b;
    --ink-dark: #333333;
    --ink-mid: #5c5c5c;
    --ink-light: #9d9d9d;
    --mark-faint: #ededed;
    --icon-bg: #8a8a8a;
  }
  * { margin: 0; padding: 0; box-sizing: border-box; }
  html, body { width: 1200px; height: 800px; overflow: hidden; }
  body {
    background: var(--backdrop);
    position: relative;
    font-family: "Open Sans", Arial, sans-serif;
  }
  .card {
    position: absolute;
    top: 257px;
    width: 500px;
    height: 286px;
    border-radius: 3px;
    overflow: hidden;
    box-shadow: 0 6px 18px rgba(0,0,0,0.22);
  }
  .card-back {
    left: 70px;
    background: var(--card-black);
    display: flex;
    flex-direction: column;
    align-items: center;
    justify-content: center;
    gap: 16px;
  }
  .brand-disc {
    width: 120px;
    height: 120px;
    border-radius: 50%;
    background: var(--card-white);
  }
  .brand-name-back {
    font-family: "Montserrat", Arial, sans-serif;
    font-weight: 700;
    font-size: 20px;
    letter-spacing: 1px;
    text-transform: uppercase;
    color: var(--card-white);
  }
  .card-front {
    left: 630px;
    background: var(--card-white);
    padding: 30px 32px;
  }
  .faint-disc {
    position: absolute;
    right: -40px;
    bottom: -70px;
    width: 210px;
    height: 210px;
    border-radius: 50%;
    background: var(--mark-faint);
  }
  .company-name {
    position: relative;
    font-family: "Montserrat", Arial, sans-serif;
    font-weight: 700;
    font-size: 30px;
    color: var(--ink-mid);
    text-transform: uppercase;
    letter-spacing: 0.5px;
    line-height: 1;
  }
  .person { position: relative; margin-top: 16px; }
  .person-name { font-weight: 700; font-size: 16px; color: var(--ink-dark); line-height: 1.1; }
  .person-role { font-size: 12px; color: var(--ink-light); line-height: 1.2; }
  .address { position: relative; margin-top: 12px; font-size: 13px; color: var(--ink-dark); line-height: 1.3; }
  .contacts { position: relative; margin-top: 10px; list-style: none; }
  .contacts li {
    display: flex;
    align-items: center;
    gap: 8px;
    font-size: 13px;
    color: var(--ink-dark);
    line-height: 1.3;
  }
  .contact-icon {
    width: 13px;
    height: 13px;
    border-radius: 2px;
    flex: none;
  }
</style>
</head>
<body>
  <section class="card card-back" aria-label="Card back">
    <div class="brand-disc"></div>
    <div class="brand-name-back">Velmora Linkway</div>
  </section>

  <section class="card card-front" aria-label="Card front">
    <div class="faint-disc"></div>
    <h1 class="company-name">Velmora Linkway</h1>
    <div class="person">
      <p class="person-name">Darren Holt</p>
      <p class="person-role">Owner</p>
    </div>
    <p class="address">P.O. Box 7384<br>Harlow Springs, M I 49568</p>
    <ul class="contacts">
      <li>
        <svg class="contact-icon" viewBox="0 0 13 13"><rect width="13" height="13" rx="2" fill="#8a8a8a"/><path d="M4 3h2l.6 2-1 .8a5 5 0 0 0 1.6 1.6l.8-1 2 .6v2A1 1 0 0 1 9 10 6 6 0 0 1 3 4a1 1 0 0 1 1-1z" fill="#fff"/></svg>
        555 204 8817
      </li>
      <li>
        <svg class="contact-icon" viewBox="0 0 13 13"><rect width="13" height="13" rx="2" fill="#8a8a8a"/><rect x="4.2" y="2.5" width="4.6" height="8" rx="0.8" fill="#fff"/><rect x="5" y="3.5" width="3" height="5" fill="#8a8a8a"/></svg>
        555 390 6142
      </li>
      <li>
        <svg class="contact-icon" viewBox="0 0 13 13"><rect width="13" height="13" rx="2" fill="#8a8a8a"/><rect x="2.5" y="4" width="8" height="5.5" fill="#fff"/><path d="M2.5 4l4 3 4-3" stroke="#8a8a8a" stroke-width="0.8" fill="none"/></svg>
        info@velmoralinkway.com
      </li>
      <li>
        <svg class="contact-icon" viewBox="0 0 13 13"><rect width="13" height="13" rx="2" fill="#8a8a8a"/><circle cx="6.5" cy="6.5" r="3.8" fill="none" stroke="#fff" stroke-width="0.9"/><path d="M2.7 6.5h7.6M6.5 2.7c-2 2.5-2 5.1 0 7.6M6.5 2.7c2 2.5 2 5.1 0 7.6" stroke="#fff" stroke-width="0.7" fill="none"/></svg>
        www.velmoralinkway.com
      </li>
    </ul>
  </section>
</body>
</html>
```